Flyer or Info graphic required -for journey map/flow chart

I would like a info graphic designed around the Australian home buying process. explaining all the steps along the way and how it a fits together from the start all the way to settlement and when you pick up the keys.

i want it to be clear and simple. there is quite a lot of words and so the design needs to be simple so they can take it all in.
I have attached an example of one i have seen to give you an idea of what i am thinking as well as the required words

Target Market(s)

25-35 year old first time home buyers

Industry/Entity Type

Financial Service

Font styles to use
Sans Serif

Colors
0355a3

Requirements
Must have
• the word document attached called "start" has the steps i want in my document.
• there is also a hand drawn picture (untitled document) with a portion in yellow, this reflects a certain stage of the process called "cooling off" and it needs to be highlighted as one stage.
• there are also days mentioned on this document so readers understand how long things take
Nice to have
• Logo and Web Address & corporate colours

```html
<!DOCTYPE html>
<html lang="en">
<head>
<meta charset="utf-8">
<title>Home Buying Journey</title>
<link rel="stylesheet" href="https://fonts.googleapis.com/css2?family=Roboto:wght@400;500;700;900&display=swap">
<style>
  :root {
    --sky-top: #1a97e0;
    --sky-bottom: #6cc9f3;
    --road: #ffffff;
    --cooling: #fbee23;
    --brand-blue: #0355a3;
    --step-blue: #1b86d3;
    --heading-blue: #1477c4;
    --heading-red: #e3262b;
    --ink: #1c1c1c;
    --navy: #1f2b47;
    --tag-yellow: #ffe800;
    --grass: #5cb536;
    --soil: #7a5230;
    --soil-dark: #3e3a36;
    --cloud: #ffffff;
  }
  * { box-sizing: border-box; margin: 0; padding: 0; }
  html, body { width: 1200px; height: 2744px; overflow: hidden; }
  body {
    position: relative;
    font-family: 'Roboto', Arial, sans-serif;
    color: var(--ink);
    background: linear-gradient(180deg, var(--sky-top) 0%, var(--sky-bottom) 88%);
  }
  .layer { position: absolute; left: 0; top: 0; width: 1200px; height: 2744px; }

  .ground-grass { position: absolute; left: 0; top: 2440px; width: 1200px; height: 50px; background: var(--grass); }
  .ground-edge { position: absolute; left: 0; top: 2490px; width: 1200px; height: 14px; background: var(--soil-dark); }
  .ground-soil { position: absolute; left: 0; top: 2504px; width: 1200px; height: 240px; background: var(--soil); }

  /* masthead */
  .masthead-title {
    position: absolute; left: 110px; top: 26px;
    font-size: 72px; font-weight: 900; color: #fff; letter-spacing: -1px; line-height: 1;
  }
  .masthead-sub {
    position: absolute; left: 112px; top: 110px;
    font-size: 23px; font-weight: 700; color: var(--tag-yellow);
  }
  .brand { position: absolute; left: 952px; top: 52px; display: flex; align-items: center; gap: 12px; }
  .brand-mark { width: 34px; height: 34px; background: #fff; }
  .brand-name { font-size: 30px; font-weight: 900; color: #fff; line-height: 1; letter-spacing: 0.5px; }

  /* placeholders */
  .art { position: absolute; }
  .art-person { background: linear-gradient(180deg, #2a3d63, #16233f); border-radius: 40px 40px 8px 8px; }
  .art-cloud { background: var(--cloud); border-radius: 40px; opacity: .95; }
  .art-house { background: linear-gradient(180deg, #e9c37a, #c9893f); border-radius: 6px; }
  .art-tree { background: linear-gradient(180deg, #8ccf3e, #4c9a2a); border-radius: 60px 60px 10px 10px; }
  .art-icon { background: #dfe9f3; border-radius: 8px; }
  .art-pizza { background: linear-gradient(135deg, #f5b942, #e0702a); border-radius: 50%; }

  /* steps */
  .badge {
    position: absolute; width: 50px; height: 50px;
    background: var(--step-blue); color: #fff;
    font-size: 32px; font-weight: 900; line-height: 50px; text-align: center;
  }
  .step-title { position: absolute; font-size: 20px; font-weight: 700; color: var(--heading-blue); line-height: 1.15; text-align: center; }
  .step-title.is-cooling { color: var(--heading-red); }
  .step-text { position: absolute; font-size: 16px; line-height: 1.25; }
  .step-text.small { font-size: 15px; }
  .step-list { list-style: none; }
  .step-list li { position: relative; padding-left: 18px; margin-bottom: 2px; }
  .step-list li::before {
    content: ""; position: absolute; left: 2px; top: 6px;
    width: 9px; height: 9px; border-radius: 50%; background: var(--step-blue);
  }
  .step-list.is-cooling li::before { background: var(--heading-red); }

  .day-tag {
    position: absolute; padding: 6px 14px;
    background: var(--tag-yellow); color: var(--ink);
    font-size: 22px; font-weight: 700; line-height: 1;
  }
  .cooling-label {
    position: absolute; left: 915px; top: 1250px; width: 268px; height: 62px;
    background: var(--cooling); color: var(--heading-blue);
    font-size: 42px; font-weight: 900; text-align: center; line-height: 62px;
  }
  .note {
    position: absolute; display: flex; align-items: center; gap: 12px;
    background: var(--navy); color: #fff; border-radius: 8px;
    padding: 8px 16px; font-size: 17px; line-height: 1.25;
  }
  .note .note-lead { color: var(--tag-yellow); }
  .note svg { flex: none; }
  .start-word {
    position: absolute; left: 905px; top: 262px;
    font-size: 56px; font-weight: 900; color: var(--brand-blue); line-height: 1;
  }
</style>
</head>
<body>

  <div class="ground-grass"></div>
  <div class="ground-edge"></div>
  <div class="ground-soil"></div>

  <div class="art art-cloud" role="img" aria-label="White cloud" style="left:60px;top:602px;width:220px;height:38px"></div>
  <div class="art art-cloud" role="img" aria-label="White cloud" style="left:600px;top:1044px;width:200px;height:36px"></div>
  <div class="art art-tree" role="img" aria-label="Leafy green tree" style="left:60px;top:2260px;width:160px;height:190px"></div>
  <div class="art art-tree" role="img" aria-label="Leafy green tree" style="left:1020px;top:2200px;width:160px;height:150px"></div>

  <svg class="layer" viewBox="0 0 1200 2744" aria-hidden="true">
    <polygon points="70,20 935,20 935,152 40,152 40,48" fill="var(--navy)"/>

    <path d="M 900 290 H 210 A 110 110 0 0 0 210 510 H 920 A 110 110 0 0 1 920 730 H 210 A 110 110 0 0 0 210 950 H 920 A 110 110 0 0 1 920 1170 H 210 A 110 110 0 0 0 210 1390 H 920 A 110 110 0 0 1 920 1610 H 210 A 110 110 0 0 0 210 1830 H 920 A 110 110 0 0 1 920 2050 H 260 A 190 190 0 0 0 260 2430 H 920 A 110 110 0 0 1 920 2650 H 40"
          fill="none" stroke="var(--road)" stroke-width="176"/>
    <path d="M 700 950 H 920 A 110 110 0 0 1 920 1170 H 210 A 110 110 0 0 0 210 1390 H 920 A 110 110 0 0 1 920 1610 H 480"
          fill="none" stroke="var(--cooling)" stroke-width="176"/>

    <polygon points="790,290 900,180 900,228 1160,228 1160,352 900,352 900,400" fill="#fff" stroke="#bfe3f8" stroke-width="4"/>

    <polyline points="1130,858 1178,858 1178,1640 1120,1640" fill="none" stroke="#fff" stroke-width="4"/>
    <polyline points="548,1510 560,1524 572,1510" fill="none" stroke="var(--tag-yellow)" stroke-width="4"/>

    <g transform="translate(945,735)" fill="none" stroke="var(--step-blue)" stroke-width="5" stroke-linejoin="round">
      <polyline points="0,0 12,0 22,36 62,36 70,10 16,10"/>
      <circle cx="26" cy="48" r="5" fill="var(--step-blue)"/>
      <circle cx="58" cy="48" r="5" fill="var(--step-blue)"/>
    </g>
  </svg>

  <h1 class="masthead-title">Home Buying Journey</h1>
  <p class="masthead-sub">Overview to help understand all the steps in buying your first HOME</p>
  <div class="brand">
    <span class="brand-mark"></span>
    <span class="brand-name">KEYSTONE<br>LOANS</span>
  </div>

  <div class="art art-person" role="img" aria-label="Illustrated advisor in a dark suit" style="left:100px;top:178px;width:90px;height:175px"></div>
  <div class="art art-person" role="img" aria-label="Illustrated advisor in a white shirt and red tie" style="left:1100px;top:170px;width:85px;height:180px"></div>
  <div class="start-word">START</div>
  <div class="art art-icon" role="img" aria-label="Contract document icon" style="left:1000px;top:602px;width:50px;height:50px"></div>
  <div class="art art-house" role="img" aria-label="Small house with a picket fence" style="left:425px;top:576px;width:130px;height:62px"></div>
  <div class="art art-icon" role="img" aria-label="Bank building icon" style="left:30px;top:1250px;width:88px;height:74px"></div>
  <div class="art art-icon" role="img" aria-label="Envelope with letter icon" style="left:940px;top:1626px;width:70px;height:54px"></div>
  <div class="art art-pizza" role="img" aria-label="Pizza slice illustration" style="left:205px;top:2205px;width:72px;height:64px"></div>
  <div class="art art-house" role="img" aria-label="Family house with red door, white picket fence and garden" style="left:380px;top:2150px;width:300px;height:290px"></div>
  <div class="art art-icon" role="img" aria-label="Online payment on a computer screen" style="left:905px;top:2604px;width:100px;height:70px"></div>

  <!-- step 1 -->
  <div class="badge" style="left:495px;top:170px">1</div>
  <h2 class="step-title" style="left:250px;top:228px;width:540px">Start “Living Like You Have a Mortgage”</h2>
  <ul class="step-text step-list" style="left:250px;top:256px;width:540px">
    <li>We can work together to understand how much you can borrow, and you can start putting all the elements in place to be ready for the pre-approval.</li>
    <li>Your savings plan will look a lot like your future loan repayments.</li>
  </ul>

  <div class="note" style="left:300px;top:382px;width:560px;height:46px">
    <svg width="20" height="26" viewBox="0 0 20 26"><circle cx="10" cy="10" r="9" fill="var(--tag-yellow)"/><rect x="6" y="19" width="8" height="6" fill="#c9c9c9"/></svg>
    <span><span class="note-lead">Idea:</span> Get the checklist from <b>www.keystonehomeloans.com.au</b></span>
  </div>

  <!-- step 2 -->
  <div class="badge" style="left:100px;top:486px">2</div>
  <ul class="step-text step-list" style="left:168px;top:448px;width:330px">
    <li>Make an appointment to talk to me. We will discuss lender, interest rates fees &amp; different options.</li>
    <li>We select the lender and tell them what we want.</li>
  </ul>

  <!-- step 3 -->
  <div class="badge" style="left:925px;top:440px">3</div>
  <h2 class="step-title" style="left:530px;top:448px;width:380px">Appoint your Conveyancer</h2>
  <ul class="step-text step-list" style="left:530px;top:476px;width:385px">
    <li>Make sure you understand their cost (ask them if this includes reviewing a contract or two).</li>
    <li>Ask them – “what do I do once my offer is accepted?”</li>
  </ul>

  <!-- step 4 -->
  <div class="badge" style="left:1085px;top:705px">4</div>
  <h2 class="step-title" style="left:895px;top:668px;width:170px">Time to go shopping</h2>

  <!-- step 5 -->
  <div class="badge" style="left:590px;top:614px">5</div>
  <h2 class="step-title" style="left:340px;top:672px;width:540px">Making an offer</h2>
  <ul class="step-text step-list" style="left:350px;top:700px;width:530px">
    <li>Have you done your research? Get a Property Profile report.</li>
    <li>Start low.</li>
    <li>Ask the agent “what happens if my offer is accepted?”</li>
  </ul>
  <h2 class="step-title" style="left:170px;top:702px;width:130px">Make an offer</h2>

  <div class="note" style="left:300px;top:810px;width:690px;height:64px">
    <svg width="20" height="26" viewBox="0 0 20 26"><circle cx="10" cy="10" r="9" fill="var(--tag-yellow)"/><rect x="6" y="19" width="8" height="6" fill="#c9c9c9"/></svg>
    <span><span class="note-lead">Remember</span> – it is possible to also negotiate a smaller deposit (eg 5%) and longer cooling off period and or a longer Settlement period.</span>
  </div>

  <!-- step 6 -->
  <div class="badge" style="left:70px;top:884px">6</div>
  <ul class="step-text step-list" style="left:140px;top:890px;width:545px">
    <li>Your offer is not binding until you sign the contract and pay the deposit, you are ‘just’ making an offer and you can change your mind.</li>
    <li>Make sure your conveyancer has seen the contract before you sign it.</li>
  </ul>

  <!-- step 7 -->
  <div class="day-tag" style="left:1030px;top:840px">Day 1</div>
  <div class="badge" style="left:1112px;top:1040px">7</div>
  <h2 class="step-title is-cooling" style="left:712px;top:882px;width:215px">Offer Accepted</h2>
  <ul class="step-text small step-list is-cooling" style="left:712px;top:908px;width:210px">
    <li>I need the contract and purchase price as soon as its accepted – I also need your conveyancers details.</li>
  </ul>
  <ul class="step-text small step-list is-cooling" style="left:928px;top:962px;width:160px">
    <li>Sign the contract &amp; pay your deposit (‘Normally’ 0.25% of the purchase price)</li>
  </ul>
  <p class="step-text small" style="left:708px;top:1100px;width:215px">Contracts are then “Exchanged” – and Cooling Off starts (normally 5 days)</p>

  <div class="cooling-label">Cooling off</div>

  <!-- step 8 -->
  <div class="badge" style="left:460px;top:1058px">8</div>
  <h2 class="step-title is-cooling" style="left:180px;top:1114px;width:500px">Final Instructions to your Lender</h2>
  <ul class="step-text step-list is-cooling" style="left:185px;top:1142px;width:495px">
    <li>We now finalise the loan amount plus the structure (i.e fixed or variable rates)</li>
    <li>I instruct the Lender on what we want done.</li>
    <li>A Valuation is ordered.</li>
  </ul>

  <!-- step 9 -->
  <div class="badge" style="left:470px;top:1278px">9</div>
  <h2 class="step-title is-cooling" style="left:175px;top:1336px;width:515px">Strata Report / Building Report</h2>
  <ul class="step-text step-list is-cooling" style="left:185px;top:1364px;width:505px">
    <li>If you are buying a Unit – you need a strata report done.</li>
    <li>If you are buying a house – you need a Pest &amp; Building Report.</li>
  </ul>

  <!-- step 10 -->
  <div class="badge" style="left:790px;top:1278px">10</div>
  <h2 class="step-title is-cooling" style="left:712px;top:1336px;width:210px">Formal Approval</h2>
  <ul class="step-text small step-list is-cooling" style="left:712px;top:1362px;width:205px">
    <li>When the Valuation is back (3 days) the bank will issue the Formal Approval.</li>
  </ul>
  <ul class="step-text small step-list is-cooling" style="left:925px;top:1420px;width:160px">
    <li>Your broker will email you a copy and provide one to your Conveyancer.</li>
  </ul>

  <!-- step 11 -->
  <div class="day-tag" style="left:500px;top:1468px">Day 5</div>
  <div class="badge" style="left:690px;top:1496px">11</div>
  <h2 class="step-title is-cooling" style="left:495px;top:1558px;width:390px">Cooling Off Expires</h2>
  <ul class="step-text step-list is-cooling" style="left:505px;top:1586px;width:375px">
    <li>Now that you have your Approval and your reports are all ok, Cooling can expire and the contract becomes “Formal”.</li>
  </ul>

  <!-- step 12 -->
  <div class="badge" style="left:345px;top:1496px">12</div>
  <h2 class="step-title" style="left:170px;top:1552px;width:300px">Lender Prepares Loan Documents</h2>
  <ul class="step-text small step-list" style="left:160px;top:1604px;width:305px">
    <li>Work with your broker to make sure they are correct and you understand all the documents before you sign.</li>
  </ul>
  <ul class="step-text small step-list" style="left:40px;top:1692px;width:150px">
    <li>Return the signed documents to the Lender.</li>
  </ul>

  <!-- step 13 -->
  <div class="badge" style="left:385px;top:1716px">13</div>
  <h2 class="step-title" style="left:300px;top:1772px;width:200px;font-size:18px">Lender Reviews Documents and is “ready to book settlement”</h2>

  <!-- step 14 -->
  <div class="badge" style="left:690px;top:1716px">14</div>
  <div class="day-tag" style="left:858px;top:1700px">Day 40</div>
  <h2 class="step-title" style="left:520px;top:1774px;width:360px">Settlement is Booked</h2>
  <ul class="step-text step-list" style="left:540px;top:1802px;width:340px">
    <li>Your conveyancer will coordinate this with everyone.</li>
  </ul>

  <!-- step 15 -->
  <h2 class="step-title" style="left:900px;top:1776px;width:140px;font-size:18px">Cheque Directions</h2>
  <div class="badge" style="left:1115px;top:1992px">15</div>
  <ul class="step-text small step-list" style="left:945px;top:1822px;width:158px">
    <li>A big job for your conveyancer to get right. What has been paid, who needs to be paid and where the available money is sitting.</li>
  </ul>
  <ul class="step-text step-list" style="left:565px;top:1994px;width:350px">
    <li>You may have more savings to contribute at this stage – this is where you get the exact number.</li>
  </ul>

  <div class="note" style="left:160px;top:1918px;width:760px;height:46px">
    <svg width="20" height="26" viewBox="0 0 20 26"><circle cx="10" cy="10" r="9" fill="var(--tag-yellow)"/><rect x="6" y="19" width="8" height="6" fill="#c9c9c9"/></svg>
    <span><span class="note-lead">Idea:</span> Ask them if you transfer it to their trust account or do you need a bank cheque?</span>
  </div>

  <!-- step 16 -->
  <div class="day-tag" style="left:28px;top:1924px">Day 42</div>
  <div class="badge" style="left:66px;top:2112px">16</div>
  <h2 class="step-title" style="left:190px;top:1986px;width:330px">Settlement</h2>
  <ul class="step-text small step-list" style="left:200px;top:2012px;width:330px">
    <li>Your Conveyancer will contact you as soon as its done.</li>
    <li>Pick up the keys for the Estate Agent.</li>
    <li>Pizza party at your place!!!</li>
  </ul>

  <!-- step 17 -->
  <div class="badge" style="left:790px;top:2312px">17</div>
  <h2 class="step-title" style="left:712px;top:2368px;width:230px">Internet banking and account set up</h2>
  <ul class="step-text small step-list" style="left:712px;top:2420px;width:225px">
    <li>This may take your Lender 7-10 days after settlement.</li>
  </ul>
  <ul class="step-text small step-list" style="left:940px;top:2468px;width:150px">
    <li>Be proactive and call them so you know how everything works.</li>
  </ul>

  <!-- step 18 -->
  <div class="badge" style="left:60px;top:2624px">18</div>
  <h2 class="step-title" style="left:125px;top:2636px;width:160px">First Payment</h2>
  <ul class="step-text step-list" style="left:305px;top:2590px;width:590px">
    <li>Normally 1 month after settlement.</li>
    <li>The Lender often messes this up – so take control, it is your loan and you do it how you want.</li>
    <li>Set up a payment date that suits you – ie change to weekly or fortnightly (like your pay) &amp; make it the day after your pay.</li>
  </ul>

</body>
</html>
```